3D printers services needs a brochure

We need a Creative, Innovative idea for a brochure. 3d printing for Prototyping, .
We would like to have an A4 horizontal brochure that could give a 3D effect when folded or cut.
Our name is K7! Spark! Build! Soar! our website is www.k7momentum.com. Please be inspired by our logo and the dreamy cloud part.
Our prospects: Architects, Artists, Museums and Designers ( Jewellery, watches, etc ...)
What we offer:
.3D printing and prototyping.
.3D scanning.
.Transforming 2D images to 3D objects.
. Making their Portals where clients can visualize, personalize (IN 3D) and order their work.

Reason: I would like to extend it because i figured out the deadline is too short! Thank you Best regards Fadri

Printing

```html
<!DOCTYPE html>
<html lang="en">
<head>
<meta charset="utf-8">
<title>K7 Brochure</title>
<link href="https://fonts.googleapis.com/css2?family=Open+Sans:wght@400;600&family=Roboto+Condensed:wght@400;700&family=Bitter:wght@400;500&family=Questrial&display=swap" rel="stylesheet">
<style>
:root{
  --green:#7fd41c;
  --green-dark:#5fb014;
  --green-light:#9be23f;
  --cyan:#3fd8ec;
  --cyan-text:#2fc6e0;
  --ink:#222;
  --gray:#6b6b6b;
  --paper:#fff;
  --stage:#ececec;
  --photo-dark:#2b2b2b;
  --photo-darker:#1e1e1e;
  --photo-warm:#4e3d42;
  --photo-light:#f1f1f1;
}
*{margin:0;padding:0;box-sizing:border-box}
html,body{width:686px;height:1200px;overflow:hidden}
body{background:var(--stage);font-family:"Open Sans",sans-serif;color:var(--ink);position:relative}
.sheet{position:absolute;background:var(--paper);box-shadow:0 2px 8px rgba(0,0,0,.15)}
.sheet-front{left:22px;top:40px;width:642px;height:500px}
.sheet-back{left:18px;top:600px;width:650px;height:507px}
.abs{position:absolute}
.panel-green{background:linear-gradient(180deg,var(--green) 0%,var(--green-light) 40%,var(--green) 100%)}
.photo{position:absolute}
.heading{font-family:"Roboto Condensed",sans-serif;font-weight:700;color:var(--green-dark)}
.heading-rule{border-bottom:1px solid #ddd;padding-bottom:1px}
.offer-list{list-style:none;font-size:7.5px;line-height:1.35}
.offer-list li{position:relative;padding-left:12px;margin-bottom:7px}
.offer-list li::before{content:"";position:absolute;left:0;top:2px;width:6px;height:6px;background:var(--green);border-radius:1px}
.call-pill{position:absolute;border-radius:22px;text-align:center;font-family:"Roboto Condensed",sans-serif;line-height:1.15;box-shadow:0 2px 4px rgba(0,0,0,.25)}
.call-pill .label{font-size:12px;display:block;padding-top:7px}
.call-pill .number{font-size:16px;display:block}
.call-cyan{background:var(--cyan);color:#0b3b45}
.call-green{background:linear-gradient(180deg,var(--green-light),var(--green-dark));color:#fff}
.brand{position:absolute;display:flex;align-items:center;justify-content:center;gap:8px;font-family:"Questrial",sans-serif;color:#8a8a8a}
.brand .mark{width:14px;height:14px;background:var(--green)}
.brand .name{font-size:54px;line-height:1}
.tagline{position:absolute;font-family:"Questrial",sans-serif;letter-spacing:1px;text-align:center;color:#333}
.contact{position:absolute;left:20px;color:#fff;font-size:7px;line-height:1.3}
.contact-row{display:flex;gap:6px;align-items:flex-start;margin-bottom:7px}
.contact-row svg{flex:0 0 8px;margin-top:1px}
.social{display:flex;gap:4px;margin-top:5px}
.social span{width:15px;height:15px;border-radius:50%;background:#1b5fa8;border:1.5px solid #fff}
.experts{position:absolute;left:0;width:216px;top:202px;text-align:center;font-family:"Bitter",serif;font-size:15.5px;line-height:1.55;color:var(--gray)}
.body-copy p{font-family:"Bitter",serif;font-size:7.9px;line-height:1.5;margin-bottom:7.5px}
.offer-card{position:absolute;left:0;width:215px;height:110px}
.offer-photo{position:absolute;left:84px;top:0}
.label-cloud{position:absolute;left:8px;width:108px;height:78px}
.label-cloud svg{position:absolute;left:0;top:0}
.offer-label{position:absolute;left:0;top:6px;width:108px;height:70px;display:flex;align-items:center;justify-content:center;text-align:center;font-family:"Bitter",serif;font-weight:500;font-size:10.5px;line-height:1.2;color:#111}
.partners-list li{font-family:"Bitter",serif;font-size:7.9px;line-height:1.6;margin-bottom:9px}
.url{position:absolute;font-size:8.5px;font-weight:600;text-align:center;width:216px}
</style>
</head>
<body>

<section class="sheet sheet-front">
  <div class="abs" style="left:0;top:0;width:216px;height:500px">
    <div class="photo" role="img" aria-label="Architectural 3D model of a building floor with green rooms over blueprint drawings" style="left:14px;top:16px;width:196px;height:230px;background:linear-gradient(160deg,#f2f2f2 0%,#dcdcdc 45%,#a7d96a 70%,#e6e6e6 100%)"></div>
    <p class="abs" style="left:17px;top:268px;width:190px;font-family:'Roboto Condensed',sans-serif;font-size:11.5px;line-height:1.45;color:var(--cyan-text)">Our prospects: Architects, Artists, Museums and Designers</p>
    <h2 class="heading heading-rule abs" style="left:17px;top:314px;width:110px;font-size:13px">What we offer:</h2>
    <ul class="offer-list abs" style="left:22px;top:340px;width:180px">
      <li>3D printing and prototyping</li>
      <li>3D scanning</li>
      <li>Transforming 2D images to 3D objects</li>
      <li>Making their Portals where clients can visualize, personalize (IN 3D) and order their work</li>
    </ul>
    <div class="call-pill call-cyan" style="left:22px;top:446px;width:134px;height:48px">
      <span class="label">Call Us Today</span><span class="number">4179-555-0142</span>
    </div>
  </div>

  <div class="abs panel-green" style="left:216px;top:0;width:210px;height:500px">
    <svg class="abs" style="left:8px;top:40px" width="200" height="100" viewBox="0 0 200 100" aria-hidden="true">
      <path d="M30 88 C8 88 4 64 22 58 C14 38 38 26 52 36 C60 14 92 10 104 28 C116 8 150 12 154 34 C176 28 194 46 184 62 C198 72 188 92 168 88 Z" fill="rgba(255,255,255,.12)" stroke="rgba(255,255,255,.45)" stroke-width="1.2"/>
    </svg>
    <p class="abs" style="left:20px;top:62px;width:186px;text-align:center;font-family:'Roboto Condensed',sans-serif;font-size:11.5px;line-height:1.5;color:#fff">We act<br>as your consultants<br>to offer the best tools needed<br>for your 3D projects.</p>
    <div class="brand" style="left:0;top:205px;width:210px"><span class="mark"></span><span class="name">K7</span></div>
    <p class="tagline" style="left:0;top:318px;width:210px;font-size:11.5px">SPARK! BUILD! SOAR!</p>
    <div class="contact" style="top:352px;width:180px">
      <div class="contact-row"><svg width="8" height="10" viewBox="0 0 8 10"><path d="M4 0a3.5 3.5 0 0 0-3.5 3.5C.5 6 4 10 4 10s3.5-4 3.5-6.5A3.5 3.5 0 0 0 4 0zm0 5a1.4 1.4 0 1 1 0-2.8A1.4 1.4 0 0 1 4 5z" fill="#fff"/></svg><span>Rue des Alpes 8, Lausanne 1003<br>Switzerland</span></div>
      <div class="contact-row" style="margin-top:10px;margin-bottom:3px"><svg width="9" height="7" viewBox="0 0 9 7"><rect x=".5" y=".5" width="8" height="6" fill="none" stroke="#fff"/><path d="M.5.5 4.5 4l4-3.5" fill="none" stroke="#fff"/></svg><span>Fadri@k7momentum.org</span></div>
      <div class="contact-row"><svg width="8" height="8" viewBox="0 0 8 8"><circle cx="4" cy="4" r="3.5" fill="none" stroke="#fff" stroke-width=".8"/><path d="M.5 4h7M4 .5v7" stroke="#fff" stroke-width=".6"/></svg><span>www.k7momentum.com</span></div>
      <div class="contact-row" style="margin-top:10px;margin-bottom:3px"><svg width="8" height="8" viewBox="0 0 8 8"><path d="M1.5.5 3 2.5 2 3.5c.6 1.2 1.3 1.9 2.5 2.5l1-1 2 1.5-1 1.5C3.5 7.5.5 4.5.5 1.5z" fill="#fff"/></svg><span>4179 555 0142</span></div>
      <div class="contact-row"><svg width="8" height="8" viewBox="0 0 8 8"><rect x="2" y=".5" width="4" height="2.5" fill="none" stroke="#fff" stroke-width=".8"/><rect x=".5" y="3" width="7" height="3" fill="#fff"/><rect x="2" y="5.5" width="4" height="2" fill="none" stroke="#fff" stroke-width=".8"/></svg><span>4179 555 0142</span></div>
      <p style="margin-top:9px;border-bottom:1px solid rgba(255,255,255,.5);width:70px;padding-bottom:2px">Follow Us On</p>
      <div class="social"><span></span><span></span><span></span></div>
    </div>
  </div>

  <div class="abs" style="left:426px;top:0;width:216px;height:500px">
    <div class="brand" style="left:0;top:55px;width:216px"><span class="mark"></span><span class="name">K7</span></div>
    <p class="tagline" style="left:0;top:152px;width:216px;font-size:12.5px">SPARK! BUILD! SOAR!</p>
    <p class="experts">We Are Experts In<br>3d Designing,<br>Scanning &amp;<br>Printing Technologies.</p>
  </div>
  <svg class="abs" style="left:322px;top:312px" width="320" height="186" viewBox="0 0 320 186" role="img" aria-label="Photo of a child drawing sketches of ideas on a wall, in a cloud-shaped frame">
    <defs>
      <linearGradient id="kidPhoto" x1="0" y1="0" x2="1" y2="1">
        <stop offset="0" stop-color="#e8e8e8"/>
        <stop offset="1" stop-color="#9a9a9a"/>
      </linearGradient>
    </defs>
    <path d="M0 186 C-2 150 20 130 44 134 C44 96 84 78 110 96 C120 40 180 10 226 40 C252 10 310 24 312 70 C330 96 322 150 316 186 Z" fill="url(#kidPhoto)"/>
  </svg>
  <div class="call-pill call-green" style="left:488px;top:446px;width:120px;height:46px">
    <span class="label">Call Us Today</span><span class="number">4179-555-0142</span>
  </div>
</section>

<section class="sheet sheet-back">
  <div class="abs body-copy" style="left:0;top:0;width:219px;height:507px">
    <h2 class="heading heading-rule abs" style="left:21px;top:18px;width:90px;font-size:13px">About Us</h2>
    <div class="abs" style="left:19px;top:44px;width:196px">
      <p>K7 stands for Spark! Build! Soar!</p>
      <p>We are experts in 3D designing, scanning and printing technologies as well as Information Technology services.</p>
      <p>We are experts in 3D designing, scanning and printing technologies as well as Information Technology services.</p>
      <p>We hope to raise awareness about our planet's limited ressources and give companies and individuals the necessary tools to create a new world where we do not need to manage stocks, shipping or a" one size fits all" model.</p>
      <p>The two main activities of the company are software solutions development and training.</p>
      <p>We help companies build the information systems most suitable to their needs through understanding their business process.</p>
      <p>We act as your consultants to offer the best tools needed for your projects.</p>
      <p>Our goal is to offer a solution that is cost effective, maintainable and expandable.</p>
      <p>In some cases we would develop complete hardware/software solutions from scratch.</p>
      <p>Our clients vary from, Artists, Architects and Designers to Doctors, Teachers and even Cuisine gastronomique</p>
    </div>
    <div class="abs" role="img" aria-label="Partner badge" style="left:22px;top:427px;width:98px;height:38px;border-radius:6px;background:linear-gradient(180deg,#eaf6fb,#cfe8f3)"></div>
    <div class="abs" role="img" aria-label="Partner badge" style="left:140px;top:427px;width:66px;height:46px;background:#e4f1f5;border-radius:4px"></div>
  </div>

  <div class="abs panel-green" style="left:219px;top:0;width:215px;height:507px">
    <h2 class="abs" style="left:9px;top:18px;font-family:'Roboto Condensed',sans-serif;font-weight:700;font-size:13px;color:#fff">What We Offer:</h2>

    <div class="offer-card" style="top:28px">
      <svg class="offer-photo" width="126" height="106" viewBox="0 0 130 108" role="img" aria-label="Photo of a 3D printed object inside a printer">
        <path d="M20 108 C0 108 0 80 14 72 C6 44 30 20 54 30 C64 2 112 0 122 30 C136 50 132 90 118 108 Z" fill="var(--photo-dark)"/>
      </svg>
      <div class="label-cloud" style="top:30px">
        <svg width="108" height="78" viewBox="0 0 110 72" preserveAspectRatio="none" aria-hidden="true"><path d="M18 70 C4 70 2 50 14 44 C8 22 34 10 46 22 C54 4 86 4 92 24 C108 26 110 52 100 60 C104 70 96 70 90 70 Z" fill="#fff" stroke="#222" stroke-width="1.5"/></svg>
        <p class="offer-label">3D Printing</p>
      </div>
    </div>

    <div class="offer-card" style="top:146px">
      <svg class="offer-photo" width="126" height="106" viewBox="0 0 130 108" role="img" aria-label="Photo of 3D prototyped mechanical parts">
        <path d="M20 108 C0 108 0 80 14 72 C6 44 30 20 54 30 C64 2 112 0 122 30 C136 50 132 90 118 108 Z" fill="var(--photo-darker)"/>
      </svg>
      <div class="label-cloud" style="top:28px">
        <svg width="108" height="78" viewBox="0 0 110 72" preserveAspectRatio="none" aria-hidden="true"><path d="M18 70 C4 70 2 50 14 44 C8 22 34 10 46 22 C54 4 86 4 92 24 C108 26 110 52 100 60 C104 70 96 70 90 70 Z" fill="#fff" stroke="#222" stroke-width="1.5"/></svg>
        <p class="offer-label">3D Prototyping</p>
      </div>
    </div>

    <div class="offer-card" style="top:266px">
      <svg class="offer-photo" width="126" height="106" viewBox="0 0 130 108" role="img" aria-label="Photo of a person scanning an object with a 3D scanner">
        <path d="M20 108 C0 108 0 80 14 72 C6 44 30 20 54 30 C64 2 112 0 122 30 C136 50 132 90 118 108 Z" fill="var(--photo-warm)"/>
      </svg>
      <div class="label-cloud" style="top:30px">
        <svg width="108" height="78" viewBox="0 0 110 72" preserveAspectRatio="none" aria-hidden="true"><path d="M18 70 C4 70 2 50 14 44 C8 22 34 10 46 22 C54 4 86 4 92 24 C108 26 110 52 100 60 C104 70 96 70 90 70 Z" fill="#fff" stroke="#222" stroke-width="1.5"/></svg>
        <p class="offer-label">3D Scanning</p>
      </div>
    </div>

    <div class="offer-card" style="top:384px">
      <svg class="offer-photo" width="126" height="108" viewBox="0 0 130 112" role="img" aria-label="Illustration of a 2D image on one screen turned into a 3D image on another">
        <path d="M20 112 C0 112 0 84 14 76 C6 48 30 24 54 34 C64 4 112 2 122 32 C136 52 132 94 118 112 Z" fill="var(--photo-light)"/>
      </svg>
      <div class="label-cloud" style="top:28px;height:82px">
        <svg width="108" height="82" viewBox="0 0 110 72" preserveAspectRatio="none" aria-hidden="true"><path d="M18 70 C4 70 2 50 14 44 C8 22 34 10 46 22 C54 4 86 4 92 24 C108 26 110 52 100 60 C104 70 96 70 90 70 Z" fill="#fff" stroke="#222" stroke-width="1.5"/></svg>
        <p class="offer-label" style="top:12px;font-size:10px;line-height:1.15">Transforming<br>2D images<br>to 3D objects</p>
      </div>
    </div>
  </div>

  <div class="abs" style="left:434px;top:0;width:216px;height:507px">
    <h2 class="heading heading-rule abs" style="left:12px;top:18px;width:90px;font-size:13px">Partners</h2>
    <ul class="offer-list partners-list abs" style="left:12px;top:42px;width:196px">
      <li>We are independant to offer you the best in class products.</li>
      <li>We base our experience on a 15 years Software solutions company and the first Swiss 3D manufacturer:</li>
    </ul>
    <div class="photo" role="img" aria-label="3D rendered model of a curved glass office tower over architectural plans" style="left:12px;top:128px;width:196px;height:164px;background:linear-gradient(160deg,#fafafa 0%,#b8bcc2 45%,#eeeeee 100%)"></div>
    <div class="brand" style="left:0;top:330px;width:216px"><span class="mark"></span><span class="name">K7</span></div>
    <p class="tagline" style="left:0;top:404px;width:216px;font-size:11.5px">SPARK! BUILD! SOAR!</p>
    <div class="call-pill call-green" style="left:47px;top:424px;width:122px;height:46px">
      <span class="label">Call Us Today</span><span class="number">4179-555-0142</span>
    </div>
    <p class="url" style="left:0;top:482px">www.k7momentum.com</p>
  </div>
</section>

</body>
</html>
```